Up and coming mattress store needs a better website design

We are a family owned mattress store called QR Bedding and we are in need of a better looking website. We have started advertising online and our current website qrbeddingshop.com is really bad. We are looking for at lest 4 pages including: welcome page, about us page, our mattresses page, and contact us page. Here is a wire frame of something I was thinking of https://mockboard.example/7kq2ZP it doesn't have to be like this it is just an idea. Some must haves are: Name, Logo, at lest 3 spots for links for financing, a bigger spot for special offers, maybe the number and address for the store at the very bottom. You can submit a one page welcome design to start with and if I like it we can move on from there. Thank you for your time!

Target Market(s)

20 to 40 year olds who want to buy mattresses

Industry/Entity Type

Store

Coding

Coded - Design and coding required

Number of Pages Required

4 page

Requirements
Must have
• name, logo, 3 spots for links for our no credit check financing companies
Nice to have
• All stores addresses and numbers at the bottom: Main Store 2418 Tolliver Hwy South Houston 77590 (346)-555-0182 Smaller Store 2207 Hwy 9 Alvin Tx 77514 (281)-555-0139

```html
<!DOCTYPE html>
<html lang="en">
<head>
<meta charset="utf-8">
<title>QR Bedding – Welcome</title>
<link href="https://fonts.googleapis.com/css2?family=Roboto:wght@300;400;500;700&family=Roboto+Condensed:wght@700&display=swap" rel="stylesheet">
<style>
:root{
  --red:#e0191f;
  --red-band:#e12a2f;
  --ink:#333;
  --muted:#555;
  --topbar:#5b5b66;
  --footer:#1c1e22;
  --light:#f5f5f5;
  --white:#fff;
  --date:#e0762a;
}
*{box-sizing:border-box;margin:0;padding:0}
html,body{width:1200px;height:2510px;overflow:hidden}
body{font-family:"Roboto",Arial,sans-serif;color:var(--ink);background:var(--white);position:relative}
/* top bar */
.topbar{position:absolute;left:0;top:0;width:1200px;height:34px;background:var(--topbar);color:#eee;font-size:13px}
.topbar .store{position:absolute;left:97px;top:9px}
.topbar .links{position:absolute;right:70px;top:0;height:34px;display:flex}
.topbar .links span{display:flex;align-items:center;gap:7px;padding:0 20px;border-left:1px solid #6e6e78;height:34px}
.topbar .cart{position:absolute;right:72px;top:7px;width:20px;height:20px;border:1px solid #ddd;border-radius:50%}
/* header */
.header-contact{position:absolute;left:97px;top:88px;display:flex;gap:14px;font-size:14px;color:#555;line-height:19px}
.header-contact .ring{width:34px;height:34px;border:1px solid var(--red);border-radius:50%;display:flex;align-items:center;justify-content:center;margin-top:4px}
.brand{position:absolute;left:0;width:1200px;top:84px;display:flex;justify-content:center;align-items:center;gap:10px}
.brand .dot{width:28px;height:28px;border-radius:50%;background:var(--red)}
.brand .name{font-size:34px;font-weight:700;color:var(--red)}
.search{position:absolute;left:877px;top:84px;width:225px;height:40px;border:1px solid #e2e2e2;font-size:12px;color:#555;padding:12px}
.search svg{position:absolute;right:12px;top:13px}
/* nav */
.ribbon{position:absolute;top:186px;width:60px;height:40px;background:#e9e9e9;z-index:2}
.ribbon.l{left:45px;clip-path:polygon(0 0,100% 0,100% 100%,0 100%,25% 50%)}
.ribbon.r{left:1095px;clip-path:polygon(0 0,100% 0,75% 50%,100% 100%,0 100%)}
.nav{position:absolute;left:84px;top:174px;width:1032px;height:57px;background:var(--white);box-shadow:0 2px 6px rgba(0,0,0,.18);display:flex;z-index:3}
.nav a{display:flex;align-items:center;padding:0 36px;font-size:15px;color:#444;text-decoration:none;border-right:1px solid #eee}
/* hero */
.hero{position:absolute;left:0;top:209px;width:1200px;height:501px}
.hero .scene{position:absolute;inset:0;background:linear-gradient(100deg,#e4e2de 0%,#eeedeb 45%,#dad7d2 100%)}
.hero .arrow{position:absolute;top:220px}
.badge{position:absolute;left:482px;top:97px;width:200px;height:200px}
.badge-text{position:absolute;left:482px;top:142px;width:200px;text-align:center;color:#fff;font-family:"Roboto Condensed",sans-serif;font-weight:700}
.badge-text .s{font-size:26px;line-height:30px}
.badge-text .b{font-size:56px;line-height:56px}
.hero-title{position:absolute;left:0;width:1200px;top:308px;text-align:center;font-family:"Roboto Condensed",sans-serif;font-weight:700;font-size:50px;color:var(--red);letter-spacing:1px}
/* headings */
.section-head{display:flex;align-items:center;gap:14px;font-size:30px;font-weight:400;color:#333}
.section-head .mark{width:40px;height:40px;border-radius:50%;border:3px solid var(--red);display:flex;align-items:center;justify-content:center}
.section-head .mark i{width:22px;height:22px;border-radius:50%;background:var(--red);display:block}
.section-head em{font-style:normal;color:var(--red)}
.welcome-head{position:absolute;left:0;width:1200px;top:755px;justify-content:center}
.welcome-text{position:absolute;left:150px;width:900px;top:816px;text-align:center;font-size:12px;line-height:21px;color:#555}
.divider{position:absolute;left:420px;top:911px;width:360px;height:1px;background:#e6e6e6}
.card{position:absolute;top:949px;width:315px;text-align:center}
.card .photo{width:315px;height:188px}
.card .pin{width:40px;height:40px;border-radius:50%;background:var(--red);border:4px solid #fff;margin:-20px auto 0;position:relative}
.card h3{font-size:19px;font-weight:400;margin-top:8px;color:#333}
.card p{font-size:12px;line-height:20px;color:#555;margin-top:6px;padding:0 14px}
/* financing */
.finance{position:absolute;left:0;top:1292px;width:1200px;height:481px;background:linear-gradient(160deg,#ea3a3e,var(--red-band) 50%,#d11d22)}
.finance .deco{position:absolute;background:rgba(190,10,16,.55)}
.finance .mark{position:absolute;left:576px;top:60px;width:48px;height:48px;border-radius:50%;border:3px solid #fff;display:flex;align-items:center;justify-content:center}
.finance .mark i{width:26px;height:26px;border-radius:50%;background:#fff;display:block}
.finance h2{position:absolute;left:0;width:1200px;top:120px;text-align:center;font-size:30px;font-weight:400;color:#fff}
.fin-item{position:absolute;top:205px;width:300px;text-align:center;color:#fff}
.fin-item .ring{width:104px;height:104px;border:3px solid #fff;border-radius:50%;margin:0 auto;display:flex;align-items:center;justify-content:center}
.fin-item h3{font-size:16px;font-weight:500;margin-top:22px}
.fin-item p{font-size:12px;line-height:21px;margin-top:8px;padding:0 24px}
/* blog */
.blog{position:absolute;left:0;top:1773px;width:1200px;height:432px;background:var(--light)}
.blog-head{position:absolute;left:100px;top:56px;font-size:26px}
.blog-head .mark{width:32px;height:32px}
.blog-head .mark i{width:16px;height:16px}
.post{position:absolute;left:97px;width:520px;height:114px}
.post .thumb{position:absolute;left:0;top:0;width:188px;height:113px}
.post h4{position:absolute;left:214px;top:2px;font-size:16px;font-weight:400;color:#333}
.post .date{position:absolute;left:214px;top:34px;font-size:14px;color:var(--date)}
.post p{position:absolute;left:214px;top:60px;width:290px;font-size:12px;line-height:20px;color:#555}
.blog .feature{position:absolute;left:686px;top:85px;width:420px;height:285px}
/* footer */
.footer{position:absolute;left:0;top:2205px;width:1200px;height:251px;background:var(--footer);color:#eee}
.footer .brand-f{position:absolute;left:95px;top:98px;display:flex;align-items:center;gap:8px}
.footer .brand-f .dot{width:22px;height:22px;border-radius:50%;background:var(--red)}
.footer .brand-f .name{font-size:26px;font-weight:700;color:var(--red)}
.social{position:absolute;left:115px;top:147px;display:flex;gap:6px}
.social i{width:21px;height:21px;border:1px solid #ddd;border-radius:50%;display:block}
.footer h5{font-size:15px;font-weight:400;letter-spacing:.3px;color:#fff}
.col-news{position:absolute;left:367px;top:45px;width:260px}
.col-news p{font-size:12px;line-height:20px;margin-top:20px;color:#ddd}
.subscribe{display:flex;margin-top:20px}
.subscribe span{width:157px;height:40px;background:#fff;color:#555;font-size:12px;padding:13px 14px}
.subscribe b{width:80px;height:40px;background:var(--red);color:#fff;font-size:11px;font-weight:500;display:flex;align-items:center;justify-content:center}
.col-info{position:absolute;left:701px;top:45px}
.col-info ul{list-style:none;margin-top:18px;font-size:13px;line-height:24px;color:#ddd}
.col-contacts{position:absolute;left:909px;top:45px;width:220px}
.col-contacts .row{display:flex;gap:14px;font-size:13px;line-height:20px;color:#ddd;margin-top:18px}
.col-contacts .row svg{flex:none;margin-top:3px}
.bottombar{position:absolute;left:0;top:2456px;width:1200px;height:54px;background:var(--red);color:#fff;font-size:13px;text-align:center;line-height:54px}
</style>
</head>
<body>

<div class="topbar">
  <div class="store">Smaller Store 2207 Hwy 9 Alvin Tx 77514 (281)-555-0139</div>
  <div class="links">
    <span><svg width="13" height="10" viewBox="0 0 13 10"><rect x=".5" y=".5" width="12" height="9" fill="none" stroke="#eee"/><path d="M.5 .5l6 5 6-5" fill="none" stroke="#eee"/></svg>Contact Us</span>
    <span><svg width="10" height="12" viewBox="0 0 10 12"><path d="M2.5 5V3.5a2.5 2.5 0 015 0V5" fill="none" stroke="#eee" stroke-width="1.4"/><rect x="1" y="5" width="8" height="7" fill="#eee"/></svg>Sign In</span>
    <span><svg width="11" height="12" viewBox="0 0 11 12"><circle cx="5.5" cy="3" r="3" fill="#eee"/><path d="M0 12a5.5 5.5 0 0111 0z" fill="#eee"/></svg>Registered</span>
    <span style="width:50px"></span>
  </div>
  <div class="cart"><svg width="18" height="18" viewBox="0 0 18 18"><path d="M4 5h2l1.5 6h5L14 7H7" fill="none" stroke="#eee"/><circle cx="8" cy="13" r="1" fill="#eee"/><circle cx="12" cy="13" r="1" fill="#eee"/></svg></div>
</div>

<div class="header-contact">
  <div class="ring"><svg width="14" height="14" viewBox="0 0 14 14"><path d="M3 1l2 3-1.3 1.3a8 8 0 004 4L9 8l3 2-1 2.5C6 13 1 8 1.5 3z" fill="none" stroke="#e0191f" stroke-width="1.3"/></svg></div>
  <div>2418 Tolliver Hwy South Houston<br>77590 (346)-555-0182</div>
</div>
<div class="brand"><span class="dot"></span><span class="name">QR Bedding</span></div>
<div class="search">Search<svg width="12" height="12" viewBox="0 0 12 12"><circle cx="5" cy="5" r="3.8" fill="none" stroke="#333" stroke-width="1.6"/><path d="M8 8l3 3" stroke="#333" stroke-width="1.8"/></svg></div>

<div class="hero">
  <div class="scene" role="img" aria-label="Family spreading a white sheet over a new mattress in a bright bedroom"></div>
  <svg class="arrow" style="left:36px" width="30" height="60" viewBox="0 0 30 60"><path d="M26 2L4 30l22 28" fill="none" stroke="#fff" stroke-width="2"/></svg>
  <svg class="arrow" style="left:1134px" width="30" height="60" viewBox="0 0 30 60"><path d="M4 2l22 28L4 58" fill="none" stroke="#fff" stroke-width="2"/></svg>
  <svg class="badge" viewBox="0 0 200 200">
    <polygon fill="#e0191f" points="100,0 113,16 131,5 137,25 158,20 157,41 178,43 170,62 190,71 176,86 193,100 176,114 190,129 170,138 178,157 157,159 158,180 137,175 131,195 113,184 100,200 87,184 69,195 63,175 42,180 43,159 22,157 30,138 10,129 24,114 7,100 24,86 10,71 30,62 22,43 43,41 42,20 63,25 69,5 87,16"/>
    <circle cx="100" cy="100" r="74" fill="none" stroke="#fff" stroke-width="1.5" stroke-dasharray="3 3"/>
  </svg>
  <div class="badge-text"><div class="s">AT</div><div class="b">%80</div><div class="s">RETAIL</div></div>
  <div class="hero-title">MATTRESSES</div>
</div>

<nav>
  <div class="ribbon l"></div><div class="ribbon r"></div>
  <div class="nav">
    <a href="#">Home</a><a href="#">About Mattress</a><a href="#">Our Mattress</a><a href="#">Special Offers</a><a href="#">Store</a><a href="#">Blog</a><a href="#" style="border:0">Contact Us</a>
  </div>
</nav>

<h1 class="section-head welcome-head"><span class="mark"><i></i></span><span>WELCOME TO <em>QR BEDDING</em></span></h1>
<p class="welcome-text">Lorem ipsum dolor sit amet, consectetur adipiscing elit, sed do eiusmod tempor incididunt ut labore et dolore magna aliqua. Ut enim ad minim veniam, quis nostrud exercitation ullamco laboris nisi ut aliquip ex ea commodo consequat. Duis aute irure dolor in reprehenderit in voluptate velit esse cillum dolore eu fugiat nulla pariatur. Excepteur sint occaecat cupidatat non proident, sunt in culpa qui officia deserunt mollit anim id est laborum</p>
<div class="divider"></div>

<div class="card" style="left:97px">
  <div class="photo" role="img" aria-label="Smiling woman resting on a soft white bed" style="background:linear-gradient(#f3efec,#e6dfd9)"></div>
  <div class="pin"></div><h3>About Mattress</h3>
  <p>Lorem ipsum dolor sit amet, consectetur adipiscing elit, sed do eiusmod tempor incididunt ut labore et dolore magna aliqua. Ut enim ad minim veniam,</p>
</div>
<div class="card" style="left:442px">
  <div class="photo" role="img" aria-label="Stack of white mattresses on a wooden floor" style="background:linear-gradient(#efebe7,#e2d8cc)"></div>
  <div class="pin"></div><h3>Our Mattress</h3>
  <p>Lorem ipsum dolor sit amet, consectetur adipiscing elit, sed do eiusmod tempor incididunt ut labore et dolore magna aliqua. Ut enim ad minim veniam,</p>
</div>
<div class="card" style="left:787px">
  <div class="photo" role="img" aria-label="Salesman showing mattress samples to a customer in the store" style="background:linear-gradient(90deg,#dccfc2,#e9e4de 50%,#d3cec8)"></div>
  <div class="pin"></div><h3>Contact Us</h3>
  <p>Lorem ipsum dolor sit amet, consectetur adipiscing elit, sed do eiusmod tempor incididunt ut labore et dolore magna aliqua. Ut enim ad minim veniam,</p>
</div>

<section class="finance">
  <div class="deco" style="left:1010px;top:45px;width:132px;height:130px"></div>
  <div class="deco" style="left:840px;top:215px;width:120px;height:125px"></div>
  <div class="deco" style="left:650px;top:350px;width:130px;height:131px"></div>
  <div class="deco" style="left:460px;top:390px;width:110px;height:91px"></div>
  <div class="mark"><i></i></div>
  <h2>LINKS FOR FINANCING</h2>
  <div class="fin-item" style="left:98px">
    <div class="ring"><svg width="44" height="30" viewBox="0 0 44 30"><rect x="2" y="2" width="40" height="26" rx="2" fill="none" stroke="#fff" stroke-width="3"/><circle cx="22" cy="15" r="6" fill="#fff"/></svg></div>
    <h3>Harbor Lease</h3>
    <p>Lorem ipsum dolor sit amet, consectetur adipising elit, sed do eiusmod tempor iunt ut labore et dolore magna aliqua. eiusmod</p>
  </div>
  <div class="fin-item" style="left:449px">
    <div class="ring"><svg width="42" height="34" viewBox="0 0 42 34"><path d="M3 2v29h37" fill="none" stroke="#fff" stroke-width="3"/><path d="M8 25l9-10 7 6 11-12" fill="none" stroke="#fff" stroke-width="3"/><path d="M30 8h6v6" fill="none" stroke="#fff" stroke-width="3"/></svg></div>
    <h3>Forward Credit</h3>
    <p>Lorem ipsum dolor sit amet, consectetur adipising elit, sed do eiusmod tempor iunt ut labore et dolore magna aliqua. eiusmod</p>
  </div>
  <div class="fin-item" style="left:799px">
    <div class="ring"><svg width="44" height="44" viewBox="0 0 44 44"><circle cx="22" cy="22" r="18" fill="none" stroke="#fff" stroke-width="8" stroke-dasharray="14 14.3"/><circle cx="22" cy="22" r="18" fill="none" stroke="#fff" stroke-width="2"/><circle cx="22" cy="22" r="9" fill="none" stroke="#fff" stroke-width="2"/></svg></div>
    <h3>Summit Pay</h3>
    <p>Lorem ipsum dolor sit amet, consectetur adipising elit, sed do eiusmod tempor iunt ut labore et dolore magna aliqua. eiusmod</p>
  </div>
</section>

<section class="blog">
  <h2 class="section-head blog-head"><span class="mark"><i></i></span>LATEST BLOG</h2>
  <article class="post" style="top:114px">
    <div class="thumb" role="img" aria-label="Family making a bed with a white sheet" style="background:linear-gradient(#ebe9e5,#d9d4ce)"></div>
    <h4>Nulla at diam ornare, aliquam urna</h4>
    <div class="date">JULY 25, 2015</div>
    <p>Nulla at diam ornare, aliquam urna vel, commodo urna. Nam id risus a est luctus consectetur quis eget libero. Suspendisse potenti.</p>
  </article>
  <article class="post" style="top:259px">
    <div class="thumb" role="img" aria-label="Couple choosing mattress samples in the showroom" style="background:linear-gradient(90deg,#dccfc2,#e9e4de 50%,#d3cec8)"></div>
    <h4>Nulla at diam ornare, aliquam urna</h4>
    <div class="date">JULY 25, 2015</div>
    <p>Nulla at diam ornare, aliquam urna vel, commodo urna. Nam id risus a est luctus consectetur quis eget libero. Suspendisse potenti.</p>
  </article>
  <div class="feature" role="img" aria-label="Three stacked mattresses with cream quilted tops" style="background:linear-gradient(170deg,#eee6d8,#e4ddd3 50%,#dfe2e6);border-radius:6px"></div>
</section>

<footer class="footer">
  <div class="brand-f"><span class="dot"></span><span class="name">QR Bedding</span></div>
  <div class="social"><i></i><i></i><i></i><i></i><i></i></div>
  <div class="col-news">
    <h5>JOIN OUR NEWSLETTER</h5>
    <p>Excepteur sint occaecat cupidatat non proident, sunt in culpa qui</p>
    <div class="subscribe"><span>Enter Name</span><b>SUBSCRIBE</b></div>
  </div>
  <div class="col-info">
    <h5>INFORMATION</h5>
    <ul><li>Shipping and payment</li><li>Prescriptions</li><li>Shipping and payment</li><li>Prescriptions</li><li>Contacts</li></ul>
  </div>
  <div class="col-contacts">
    <h5>CONTACTS</h5>
    <div class="row"><svg width="12" height="16" viewBox="0 0 12 16"><path d="M6 15S1 9 1 6a5 5 0 0110 0c0 3-5 9-5 9z" fill="#eee"/><circle cx="6" cy="6" r="2" fill="#1c1e22"/></svg><span>Main Store 2418 Tolliver Hwy South Houston</span></div>
    <div class="row"><svg width="12" height="12" viewBox="0 0 14 14"><path d="M3 1l2 3-1.3 1.3a8 8 0 004 4L9 8l3 2-1 2.5C6 13 1 8 1.5 3z" fill="#eee"/></svg><span>77590 (346)-555-0182</span></div>
    <div class="row"><svg width="12" height="10" viewBox="0 0 12 10"><rect width="12" height="10" fill="#eee"/><path d="M0 0l6 5 6-5" fill="none" stroke="#1c1e22"/></svg><span>info@qrbeddingshop.com</span></div>
  </div>
</footer>
<div class="bottombar">All Rights Reserved. Copyrights @ 2016 QR Bedding</div>

</body>
</html>
```